Creative and Fun Farm Metal Signage in the Barn

This will be featured in the farm. to make it more unique, the measurement will be 90cm x 60cm. This sign will be made by Metal and display inside the Barn. do have 2 A4 pockets available for them to slip in the cow's birth certificate. please make it fun and professional look. i have attached few photos that show rough idea of how we want it to be.

Target Market(s)

Restaurants or Hotels

Requirements
Must have
• Include 2 A4s certificate as stated, the logo and reserver for logo as well..
Nice to have
• This is a design of Signage where we will put it up in the barn.. this will consist a logo, Reserved by, and 2 A4 paper to slip in. be creative on the design

```html
<!DOCTYPE html>
<html lang="en">
<head>
<meta charset="utf-8">
<title>Ridgeback Wagyu – Barn Reservation Sign</title>
<link rel="stylesheet" href="https://fonts.googleapis.com/css2?family=Cinzel:wght@700&family=PT+Serif:wght@700&display=swap">
<style>
  :root {
    --page: #ffffff;
    --plate: #120f0b;
    --line: #ffffff;
    --gold: #d08a2e;
    --paper: #f4f0c4;
    --paper-edge: #d9d3a0;
    --ink: #111111;
  }
  html, body {
    margin: 0;
    padding: 0;
    width: 1200px;
    height: 916px;
    overflow: hidden;
    background: var(--page);
  }
  .canvas {
    position: relative;
    width: 1200px;
    height: 916px;
  }
  .sign-plate {
    position: absolute;
    left: 0;
    top: 0;
  }
  .brand-name {
    position: absolute;
    left: 403px;
    top: 299px;
    width: 392px;
    text-align: center;
    font-family: "Cinzel", serif;
    font-weight: 700;
    font-size: 34px;
    line-height: 46px;
    letter-spacing: 3px;
    color: var(--line);
    margin: 0;
  }
  .certificate-pocket {
    position: absolute;
    top: 493px;
    width: 235px;
    height: 163px;
    background: var(--line);
  }
  .certificate-pocket.left { left: 282px; }
  .certificate-pocket.right { left: 682px; }
  .certificate-slot {
    position: absolute;
    inset: 10px 12px 12px 16px;
    background: linear-gradient(160deg, var(--paper), var(--paper-edge));
  }
  .reserved {
    position: absolute;
    left: 530px;
    top: 522px;
    width: 131px;
    text-align: center;
  }
  .reserved-label {
    font-family: "Cinzel", serif;
    font-weight: 700;
    font-size: 9px;
    letter-spacing: 1px;
    color: var(--line);
    margin: 0;
    padding-bottom: 3px;
    border-bottom: 1px solid var(--gold);
    display: inline-block;
    width: 84px;
  }
  .reserved-name {
    margin-top: 14px;
    height: 76px;
    border-radius: 8px;
    background: var(--line);
    display: flex;
    align-items: center;
    justify-content: center;
    font-family: "PT Serif", serif;
    font-weight: 700;
    font-size: 19px;
    color: var(--ink);
  }
</style>
</head>
<body>
<main class="canvas">
  <svg class="sign-plate" width="1200" height="916" viewBox="0 0 1200 916" aria-hidden="true">
    <rect x="250" y="346" width="698" height="344" rx="26" fill="var(--plate)"/>
    <rect x="276" y="371" width="647" height="291" fill="none" stroke="var(--line)" stroke-width="6"/>
    <ellipse class="emblem-outer" cx="599" cy="345" rx="214" ry="130" fill="var(--plate)"/>
    <ellipse class="emblem-white-ring" cx="599" cy="345" rx="204" ry="120" fill="var(--plate)" stroke="var(--line)" stroke-width="7"/>
    <ellipse class="emblem-gold-ring" cx="599" cy="343" rx="192" ry="108" fill="var(--plate)" stroke="var(--gold)" stroke-width="5"/>
  </svg>

  <p class="brand-name">RIDGEBACK<br>WAGYU</p>

  <div class="certificate-pocket left">
    <div class="certificate-slot" role="img" aria-label="A4 pocket holding the cow's birth certificate"></div>
  </div>

  <div class="reserved">
    <p class="reserved-label">RESERVED BY:</p>
    <div class="reserved-name">JOHN DOE</div>
  </div>

  <div class="certificate-pocket right">
    <div class="certificate-slot" role="img" aria-label="A4 pocket holding the cow's birth certificate"></div>
  </div>
</main>
</body>
</html>
```